dsadasdasdasdsa

Industry/Entity Type

Mortgage Broking

Requirements
Must have
• Call-to-action button somewhere on the graphic
Nice to have
• The font of our logo is Montserrat

```html
<!DOCTYPE html>
<html lang="en">
<head>
<meta charset="UTF-8">
<title>Mortgage Broker Directory Banner</title>
<link rel="stylesheet" href="https://fonts.googleapis.com/css2?family=Montserrat:wght@700;800;900&display=swap">
<style>
  :root {
    --green-deep: #08401b;
    --green-mid: #157a34;
    --green-glow: #2aa24a;
    --ink-green: #0f4a24;
    --yellow: #f7e61b;
    --white: #ffffff;
    --red: #c9261c;
    --shell-brown: #8a5a2a;
    --skin-green: #5fbf4a;
  }
  * { margin: 0; padding: 0; box-sizing: border-box; }
  html, body { width: 1200px; height: 180px; overflow: hidden; background: var(--green-deep); }
  .banner {
    position: relative;
    width: 1200px;
    height: 180px;
    overflow: hidden;
    font-family: "Montserrat", sans-serif;
    background:
      radial-gradient(ellipse 520px 260px at 300px 90px, var(--green-glow) 0%, var(--green-mid) 40%, var(--green-deep) 100%);
  }
  .mascot {
    position: absolute;
    left: 30px;
    top: 6px;
    width: 270px;
    height: 174px;
    border-radius: 90px 90px 20px 20px;
    background: radial-gradient(ellipse at 55% 40%, var(--skin-green) 0%, #3f9a3a 45%, var(--shell-brown) 100%);
    opacity: 0.85;
  }
  .headline {
    position: absolute;
    right: 28px;
    top: 8px;
    color: var(--yellow);
    font-weight: 700;
    font-size: 28px;
    letter-spacing: 0.3px;
  }
  .band {
    position: absolute;
    left: 440px;
    right: 0;
    top: 49px;
    height: 94px;
    background: linear-gradient(90deg, rgba(255,255,255,0) 0%, rgba(255,255,255,0.85) 22%, var(--white) 40%);
  }
  .search-line {
    position: absolute;
    right: 26px;
    color: var(--ink-green);
    font-weight: 900;
    line-height: 1;
    white-space: nowrap;
    transform: scaleX(0.78);
    transform-origin: right center;
  }
  .search-line--first { top: 56px; font-size: 39px; }
  .search-line--second { top: 98px; font-size: 43px; }
  .cta {
    position: absolute;
    left: 982px;
    top: 148px;
    width: 218px;
    height: 32px;
    background: var(--red);
    border-radius: 16px 0 0 0;
    color: var(--white);
    font-weight: 800;
    font-size: 21px;
    line-height: 32px;
    text-align: center;
    text-decoration: none;
    letter-spacing: 0.3px;
  }
</style>
</head>
<body>
  <div class="banner">
    <div class="mascot" role="img" aria-label="Friendly cartoon turtle holding a small house"></div>
    <p class="headline">Need a Mortgage Broker?</p>
    <div class="band"></div>
    <p class="search-line search-line--first">SEARCH NOW ON AUSTRALIA’S</p>
    <p class="search-line search-line--second">LARGEST DIRECTORY</p>
    <a class="cta" href="#">CLICK HERE</a>
  </div>
</body>
</html>
```